Brightfold Partners Website

Brightfold Partners (BP) provide Analytics & Enterprise Performance Management (EPM) advisory & consultancy services. We are passionate about data and making a difference for our clients by working in partnership with them, helping them on their journey to becoming an Brightfold Partner. We deliver insights which give our clients a competitive edge and a much deeper understanding of their organisation.

We need a website which shows who we are, what we do and how we do it.

www.brightfold-partners.example is our very basic website at the moment. We want to completely revamp it with a corporate look

```html
<!DOCTYPE html>
<html lang="en">
<head>
<meta charset="utf-8">
<title>Brightfold Partners – Data Analytics &amp; EPM Consulting</title>
<link rel="stylesheet" href="https://fonts.googleapis.com/css2?family=Montserrat:wght@400;500;600;700;800;900&display=swap">
<style>
:root{
  --navy:#2c5069;
  --navy-dark:#23455c;
  --orange:#ee7a22;
  --gold:#eea534;
  --sky:#cfe9f8;
  --white:#ffffff;
  --text:#4a4a4a;
  --muted:#6f6f6f;
  --peach:#fde6d6;
}
*{box-sizing:border-box;margin:0;padding:0}
html,body{width:1200px;height:2912px;overflow:hidden}
body{background:var(--sky);font-family:"Montserrat",sans-serif;color:var(--text);position:relative}
.page{position:absolute;left:66px;top:60px;width:1065px;height:2772px;background:var(--white);border-radius:42px;overflow:hidden}
.abs{position:absolute}
.btn{position:absolute;display:flex;align-items:center;justify-content:center;border-radius:16px;font-size:14px;font-weight:500;white-space:nowrap}
.btn-outline-light{border:2px solid var(--white);color:var(--white)}
.btn-outline-orange{border:1.5px solid var(--orange);color:var(--orange);background:var(--white)}
.btn-orange{background:var(--orange);color:var(--white)}

/* hero */
.hero-art{left:0;top:0;width:1065px;height:524px}
.brand{left:98px;top:30px;display:flex;align-items:center;gap:12px;color:var(--white);font-weight:700;font-size:18px;line-height:20px;letter-spacing:.5px}
.brand-dot{width:44px;height:44px;border-radius:50%;border:5px solid var(--white)}
.nav{left:493px;top:48px;display:flex;gap:30px;font-size:15px;color:#333}
.nav .active{color:var(--orange)}
.hero-title{left:96px;top:205px;font-weight:900;font-size:51px;line-height:56px;letter-spacing:2px;color:var(--white)}
.hero-title span{color:var(--gold);display:block}
.hero-sub{left:97px;top:316px;color:var(--white);font-size:18px;font-weight:500;letter-spacing:.8px}

/* what we do */
.section-title{font-size:35px;font-weight:600;color:var(--navy);letter-spacing:2px}
.wwd-title{left:0;width:1065px;top:608px;text-align:center}
.wwd-text{left:225px;width:615px;top:652px;text-align:center;font-size:11.5px;line-height:17px}
.service{position:absolute;top:706px;width:273px;height:331px;background:var(--white);box-shadow:0 0 16px rgba(238,122,34,.18);text-align:center}
.service.featured{background:var(--navy);color:var(--white)}
.service-icon{margin:28px auto 0;width:96px;height:100px;border-radius:50%;background:linear-gradient(135deg,#fbd9bf,#e3e9ee)}
.featured .service-icon{background:linear-gradient(135deg,#d9e3ea,#8ea9bd)}
.service h3{margin-top:20px;font-size:16px;font-weight:600;letter-spacing:.8px;color:var(--navy)}
.featured h3{color:var(--white)}
.service p{margin:14px auto 0;width:240px;font-size:12px;line-height:17.5px;letter-spacing:.4px;color:var(--muted)}
.featured p{color:var(--white)}
.service .btn{position:relative;margin:16px auto 0;width:116px;height:30px}

/* who we are */
.who-art{left:0;top:1130px;width:1065px;height:524px}
.who-title{right:101px;top:1192px;text-align:right;color:var(--white);font-weight:900;font-size:74px;line-height:78px;letter-spacing:4px}
.who-text{right:101px;top:1354px;width:390px;text-align:right;color:var(--white);font-size:14.5px;line-height:22px}
.who-contact{right:101px;top:1481px;text-align:right;color:var(--white);font-size:16.5px;line-height:23px;font-weight:500}

/* how we do it */
.how-title{left:96px;top:1735px}
.how-intro{left:96px;top:1785px;width:420px;font-size:11.5px;line-height:17px}
.step{position:absolute;left:96px;width:430px}
.step-num{position:absolute;left:0;top:0;width:26px;height:26px;border-radius:50%;background:#eeeeee;color:#555;font-size:19px;font-weight:500;display:flex;align-items:center;justify-content:center}
.step h4{margin-left:36px;font-size:18px;font-weight:500;color:var(--orange)}
.step p{margin-left:37px;margin-top:4px;font-size:11.5px;line-height:17px}
.how-illus{left:545px;top:1737px;width:520px;height:395px;border-radius:180px 40px 120px 200px;background:linear-gradient(140deg,#eef1f6 0%,#dfe6f2 45%,#f7d8a8 75%,#eef1f6 100%)}

/* newsletter */
.newsletter{left:98px;top:2220px;width:868px;height:191px;border-radius:0 0 60px 0;background:linear-gradient(90deg,#d9762c,#ee8a3a 50%,#d56d22)}
.newsletter h2{position:absolute;left:0;width:100%;top:26px;text-align:center;color:#fff2e4;font-size:23px;line-height:30px;font-weight:600;letter-spacing:2.5px}
.email-field{position:absolute;left:215px;top:118px;width:313px;height:29px;border:1.5px solid var(--white);border-radius:15px;color:var(--white);font-size:10px;padding-left:22px;display:flex;align-items:center}
.newsletter .btn{left:539px;top:118px;width:114px;height:29px;background:var(--white);color:var(--orange);font-size:13px;border-radius:15px}

/* footer */
.footer-brand{left:98px;top:2540px;display:flex;align-items:center;gap:12px;font-size:22px;line-height:26px;font-weight:700;color:var(--navy)}
.footer-brand .dot{width:30px;height:30px;border-radius:50%;background:var(--navy);flex:none}
.foot-head{position:absolute;top:2495px;font-size:16px;font-weight:600;color:var(--navy);letter-spacing:.6px}
.foot-head::after{content:"";display:block;width:56px;height:2px;background:var(--orange);margin-top:6px}
.contact-line{position:absolute;left:301px;display:flex;gap:11px;font-size:12.5px;line-height:18px;color:#444}
.contact-line svg{flex:none;margin-top:2px}
.sitemap a{position:absolute;font-size:10px;color:#444;text-decoration:none}
.social{left:889px;top:2546px;display:flex;gap:5px}
.social span{width:22px;height:22px;border-radius:50%;background:var(--navy)}
.rule{left:98px;top:2700px;width:868px;height:1px;background:#cfcfcf}
.copyright{left:0;width:1065px;top:2730px;text-align:center;font-size:10px;color:var(--navy)}
</style>
</head>
<body>
<div class="page">

  <!-- hero -->
  <svg class="abs hero-art" viewBox="0 0 1065 524">
    <defs>
      <linearGradient id="heroPhoto" x1="0" y1="0" x2="1" y2="1">
        <stop offset="0" stop-color="#fbf3ea"/>
        <stop offset=".5" stop-color="#efd9bc"/>
        <stop offset="1" stop-color="#d9a24a"/>
      </linearGradient>
    </defs>
    <rect x="410" y="0" width="655" height="524" fill="url(#heroPhoto)" role="img" aria-label="Photo of a smiling consultant at a desk with a computer"/>
    <path d="M0 0H410L630 470Q650 524 600 524H0Z" fill="var(--navy)"/>
    <circle cx="810" cy="263" r="25" fill="var(--orange)"/>
    <path d="M802 251L823 263L802 275Z" fill="#fff"/>
  </svg>

  <div class="abs brand"><span class="brand-dot"></span><span>BRIGHTFOLD<br>PARTNERS</span></div>
  <nav class="abs nav">
    <span class="active">Home</span><span>Services</span><span>About Us</span><span>Contact Us</span>
  </nav>
  <div class="btn btn-outline-orange" style="left:849px;top:43px;width:116px;height:30px;font-size:15px">Get Started</div>

  <h1 class="abs hero-title">BRIGHTFOLD<span>PARTNERS</span></h1>
  <p class="abs hero-sub">Data Analytics &amp; EPM Consulting Services</p>
  <div class="btn btn-outline-light" style="left:98px;top:355px;width:115px;height:29px">SIGN UP</div>
  <div class="btn btn-outline-light" style="left:224px;top:355px;width:137px;height:29px">LEARN MORE</div>

  <!-- what we do -->
  <h2 class="abs section-title wwd-title">What We Do</h2>
  <p class="abs wwd-text">BP are a Data Analytics &amp; EPM company, specialising in the implementation and support of Business Intelligence, EPM and Data Analytics business solutions, both in the Cloud and on-premise.</p>

  <div class="service" style="left:98px">
    <div class="service-icon" role="img" aria-label="Icon of two advisors in conversation"></div>
    <h3>Advise &amp; Architect</h3>
    <p>Helping our customers understand the art of the possible and safeguarding their investments by overseeing implementations.</p>
    <div class="btn btn-outline-orange">Read More</div>
  </div>
  <div class="service featured" style="left:395px">
    <div class="service-icon" role="img" aria-label="Icon of a blueprint plan with a pencil"></div>
    <h3>Design &amp; Implement</h3>
    <p>Helping our customers understand the art of the possible and safeguarding their investments by overseeing implementations.</p>
    <div class="btn btn-orange">Read More</div>
  </div>
  <div class="service" style="left:691px">
    <div class="service-icon" role="img" aria-label="Icon of a gear with outward arrows"></div>
    <h3>Optimise &amp; Manage</h3>
    <p>Helping our customers understand the art of the possible and safeguarding their investments by overseeing implementations.</p>
    <div class="btn btn-outline-orange">Read More</div>
  </div>

  <!-- who we are -->
  <svg class="abs who-art" viewBox="0 0 1065 524">
    <defs>
      <linearGradient id="whoPhoto" x1="0" y1="0" x2="1" y2="1">
        <stop offset="0" stop-color="#e9e4dd"/>
        <stop offset=".5" stop-color="#b9ad98"/>
        <stop offset="1" stop-color="#5d5a3c"/>
      </linearGradient>
    </defs>
    <path d="M0 0H600Q630 0 615 30L400 490Q385 524 350 524H0Z" fill="url(#whoPhoto)" role="img" aria-label="Photo of colleagues working around a desktop computer showing a dashboard"/>
    <path d="M665 0H1065V524H455Q415 524 432 488Z" fill="var(--navy)"/>
  </svg>
  <h2 class="abs who-title">WHO<br>WE ARE</h2>
  <p class="abs who-text">Brightfold Partners is an exciting start-up in the Data Analytics and EPM space. Founded in 2019, BP specialise in the implementation and support of BI, EPM and Data Analytics business solutions, both in the Cloud and on-premise.</p>
  <p class="abs who-contact">Call us on 01 555 0142 or<br>email: info@brightfold-partners.example</p>
  <div class="btn btn-outline-light" style="left:828px;top:1548px;width:137px;height:28px">LEARN MORE</div>

  <!-- how we do it -->
  <h2 class="abs section-title how-title">How We Do It</h2>
  <p class="abs how-intro">BP are a Data Analytics &amp; EPM company, specialising in the implementation and support of Business Intelligence, EPM and Data Analytics business solutions, both in the Cloud and on-premise.</p>
  <div class="step" style="top:1857px"><span class="step-num">1</span><h4>Lorem Ipsum</h4><p>BP are a Data Analytics &amp; EPM company, specialising in the implementation and support of Business Intelligence,</p></div>
  <div class="step" style="top:1937px"><span class="step-num">2</span><h4>Lorem Ipsum</h4><p>BP are a Data Analytics &amp; EPM company, specialising in the implementation and support of Business Intelligence,</p></div>
  <div class="step" style="top:2017px"><span class="step-num">3</span><h4>Lorem Ipsum</h4><p>BP are a Data Analytics &amp; EPM company, specialising in the implementation and support of Business Intelligence,</p></div>
  <div class="btn btn-orange" style="left:98px;top:2096px;width:115px;height:29px">Read More</div>
  <div class="abs how-illus" role="img" aria-label="Isometric illustration of an analyst at a laptop surrounded by charts, graphs and coins"></div>

  <!-- newsletter -->
  <section class="abs newsletter" role="img" aria-label="Orange-tinted photo of business people with financial figures">
    <h2>Subscribe to our Newsletter<br>and stay updated</h2>
    <div class="email-field">Email Address</div>
    <div class="btn">Subscribe</div>
  </section>

  <!-- footer -->
  <div class="abs footer-brand"><span class="dot"></span><span>Brightfold<br>Partners</span></div>

  <div class="foot-head" style="left:301px">Get In Touch</div>
  <div class="contact-line" style="top:2546px">
    <svg width="14" height="12" viewBox="0 0 14 12"><path d="M0 2L4 0L10 2L14 0V10L10 12L4 10L0 12Z" fill="var(--navy)"/></svg>
    <span>14 Harbour Row, Millbrook,<br>Dublin 8, D08 KQ41</span>
  </div>
  <div class="contact-line" style="top:2596px">
    <svg width="14" height="11" viewBox="0 0 14 11"><rect width="14" height="11" rx="1" fill="var(--navy)"/><path d="M1 1L7 6L13 1" stroke="#fff" stroke-width="1.3" fill="none"/></svg>
    <span>+01 555 0142</span>
  </div>
  <div class="contact-line" style="top:2631px">
    <svg width="14" height="14" viewBox="0 0 14 14"><path d="M3 0L5.5 3.5L4 5Q5.5 8.5 9 10L10.5 8.5L14 11L12 14Q3 13 0 2Z" fill="var(--navy)"/></svg>
    <span>info@brightfold-partners.example</span>
  </div>

  <div class="foot-head" style="left:610px">SiteMap</div>
  <div class="sitemap">
    <a style="left:611px;top:2543px">Home</a>
    <a style="left:611px;top:2571px">Services</a>
    <a style="left:611px;top:2598px">About Us</a>
    <a style="left:611px;top:2626px">Contact Us</a>
    <a style="left:697px;top:2543px">Advise &amp; Architect</a>
    <a style="left:697px;top:2571px">Design &amp; Implement</a>
    <a style="left:697px;top:2598px">Optimse &amp; Manage</a>
  </div>

  <div class="foot-head" style="left:888px">Connect</div>
  <div class="abs social" aria-label="Social network links"><span></span><span></span><span></span></div>

  <div class="abs rule"></div>
  <p class="abs copyright">Copyright all rights reserved © 2022 Brightfold Partners.</p>
</div>
</body>
</html>
```